Photoshop Design

Hi, you did a project for me a while ago as per the below description. Can you do the same again with this screen shot?
"We have a charting software application and we are in the process of upgrading our marketing.
We need our application charting screen re-created in photoshop with all components on separate layers so we can tinker with them later such as highlight particular components we are discussing and the likes.
We need the native photoshop file as the project output"
Target Market(s)
Myself
Requirements
Must have
- Look like the sample provided with layers for later editing.

```html
<!DOCTYPE html>
<html lang="en">
<head>
<meta charset="utf-8">
<title>Test Health – Subsea Tree #4</title>
<link rel="stylesheet" href="https://fonts.googleapis.com/css2?family=Roboto:wght@400;500;700&family=Roboto+Mono:wght@400;500&display=swap">
<style>
  :root{
    --bg:#303030;
    --panel:#272727;
    --strip:#222222;
    --topbar:#1676b8;
    --button:#333333;
    --button-line:#3e3e3e;
    --active:#1f8f3c;
    --dial:#262626;
    --readout:#1d1d1d;
    --blue:#2f8fe0;
    --blue-soft:#4aa3df;
    --green:#27c93f;
    --red:#d62b2b;
    --pink:#e2277a;
    --teal-band:#173a42;
    --plot:#141414;
    --period:#1a78b8;
    --text:#e6e6e6;
    --muted:#9a9a9a;
    --callout:#f5e400;
  }
  *{box-sizing:border-box;margin:0;padding:0}
  html,body{width:1200px;height:675px;overflow:hidden;background:var(--bg)}
  body{position:relative;font-family:"Roboto",sans-serif;color:var(--text)}
  .top-bar{position:absolute;left:0;top:0;width:1200px;height:22px;background:var(--topbar);font-size:12px;color:#fff}
  .top-bar .brand{position:absolute;left:8px;top:2px;font-weight:700;font-size:15px;letter-spacing:1px}
  .top-bar .user{position:absolute;left:344px;top:3px;display:flex;align-items:center;gap:8px}
  .top-bar .avatar{width:16px;height:16px;background:#cfd6dc}
  .top-bar .asset{position:absolute;left:760px;top:4px}
  .top-bar .status{position:absolute;right:8px;top:1px;font-size:15px;display:flex;gap:8px;align-items:center}
  .battery{width:9px;height:14px;border:1.5px solid #fff;border-radius:1px;position:relative}
  .battery::after{content:"";position:absolute;left:1px;right:1px;bottom:1px;height:70%;background:#fff}
  .side-strip{position:absolute;top:22px;bottom:0;width:22px;background:var(--strip);font-size:10px;color:var(--blue-soft)}
  .side-strip.left{left:0}
  .side-strip.right{right:0;width:26px}
  .side-strip .strip-label{position:absolute;top:48px;left:5px;writing-mode:vertical-rl}
  .side-strip.right .strip-label{left:8px}
  .strip-dot{position:absolute;top:6px;left:5px;width:13px;height:13px;border-radius:50%;background:#fff}
  .side-strip.right .strip-dot{left:7px}
  .breadcrumb{position:absolute;left:42px;top:30px;font-size:11px;color:var(--blue-soft);display:flex;align-items:center;gap:9px}
  .breadcrumb .dot{width:13px;height:13px;border-radius:50%;background:#fff}
  .controls{position:absolute;left:1071px;top:22px;width:103px;height:653px;background:var(--panel)}
  .control-btn{position:absolute;left:3px;width:94px;height:40px;background:var(--button);border:1px solid var(--button-line);font-size:13px;color:var(--text);display:flex;align-items:center;justify-content:center;text-align:center;line-height:1.25}
  .control-btn.active{background:var(--active);color:#fff}
  .control-btn.disabled{background:#252525;color:#4a4a4a}
  .stage{position:absolute;left:0;top:0}
  .stage text{font-family:"Roboto",sans-serif}
  .stage .mono{font-family:"Roboto Mono",monospace}
</style>
</head>
<body>
  <header class="top-bar">
    <span class="brand">VANTRA</span>
    <span class="user"><span class="avatar"></span>Sam Porter</span>
    <span class="asset">Subsea Tree #4</span>
    <span class="status"><span>10:06 PM</span><span class="battery"></span><span>85 %</span></span>
  </header>

  <nav class="side-strip left"><span class="strip-dot"></span><span class="strip-label">Main Menu</span></nav>
  <nav class="side-strip right"><span class="strip-dot"></span><span class="strip-label">Controls</span></nav>

  <div class="breadcrumb"><span class="dot"></span>Test Health</div>

  <svg class="stage" width="1200" height="675" viewBox="0 0 1200 675">
    <!-- sensor readout -->
    <g class="sensor-gauge">
      <rect x="42" y="79" width="190" height="106" rx="10" fill="var(--dial)"/>
      <text x="66" y="100" font-size="16" fill="var(--text)">SENSOR</text>
      <rect x="53" y="112" width="172" height="57" rx="3" fill="var(--readout)"/>
      <text x="213" y="158" font-size="38" text-anchor="end" fill="var(--blue)" class="mono">839.0</text>
      <circle cx="313" cy="146" r="92" fill="var(--dial)"/>
      <path d="M263.5 195.5 A70 70 0 0 1 313 76" fill="none" stroke="#2aa6e8" stroke-width="10"/>
      <path d="M313 76 A70 70 0 0 1 378.8 122.1" fill="none" stroke="var(--green)" stroke-width="10"/>
      <path d="M382 158.2 A70 70 0 0 1 373.6 181" fill="none" stroke="var(--red)" stroke-width="5"/>
      <path d="M268 191 A64 64 0 1 1 358 191" fill="none" stroke="#6a6a6a" stroke-width="4" pathLength="100" stroke-dasharray="0.4 2.1"/>
      <g font-size="7" fill="var(--muted)" text-anchor="middle">
        <text x="258" y="200">0</text><text x="233" y="165">138</text><text x="237" y="116">275</text>
        <text x="266" y="79">413</text><text x="313" y="65">550</text><text x="360" y="79">688</text>
        <text x="389" y="116">825</text><text x="393" y="165">963</text><text x="368" y="200">1100</text>
      </g>
      <line x1="313" y1="146" x2="371" y2="130.5" stroke="#e8e8e8" stroke-width="2"/>
      <circle cx="313" cy="146" r="11" fill="#3a3a3a" stroke="#e8e8e8" stroke-width="2"/>
      <text x="313" y="183" font-size="14" text-anchor="middle" fill="var(--text)">psi</text>
      <rect x="291" y="196" width="44" height="17" rx="2" fill="var(--readout)"/>
      <text x="313" y="209" font-size="13" text-anchor="middle" fill="var(--pink)" class="mono">30.1</text>
      <text x="313" y="224" font-size="8" text-anchor="middle" fill="var(--text)">deg C</text>
    </g>

    <!-- change gauge -->
    <g class="dial-gauge">
      <circle cx="501" cy="146" r="86" fill="var(--dial)"/>
      <path d="M457.2 189.8 A62 62 0 1 1 544.8 189.8" fill="none" stroke="var(--blue-soft)" stroke-width="5" pathLength="100" stroke-dasharray="0.4 2.1"/>
      <rect x="496" y="76" width="11" height="9" fill="var(--green)"/>
      <path d="M497 92 l4 -6 l4 6z" fill="#ddd"/>
      <text x="501" y="100" font-size="5" text-anchor="middle" fill="var(--muted)">TEST SPEC</text>
      <g font-size="7" fill="var(--muted)" text-anchor="middle">
        <text x="452" y="198">-70</text><text x="431" y="149">-45</text><text x="452" y="99">-25</text>
        <text x="501" y="74">-10</text><text x="551" y="99">5</text><text x="571" y="149">25</text><text x="551" y="198">50</text>
      </g>
      <text x="501" y="124" font-size="15" text-anchor="middle" fill="var(--text)">CHANGE</text>
      <rect x="452" y="132" width="99" height="31" rx="3" fill="#3a3a3a"/>
      <text x="543" y="155" font-size="22" text-anchor="end" fill="#fff" class="mono">-5.3</text>
      <text x="501" y="181" font-size="14" text-anchor="middle" fill="var(--text)">psi</text>
    </g>

    <!-- rate gauge -->
    <g class="dial-gauge">
      <circle cx="691" cy="146" r="86" fill="var(--dial)"/>
      <path d="M647.2 189.8 A62 62 0 1 1 734.8 189.8" fill="none" stroke="var(--blue-soft)" stroke-width="5" pathLength="100" stroke-dasharray="0.4 2.1"/>
      <rect x="686" y="76" width="11" height="9" fill="var(--green)"/>
      <path d="M687 92 l4 -6 l4 6z" fill="#ddd"/>
      <text x="691" y="100" font-size="5" text-anchor="middle" fill="var(--muted)">TEST SPEC</text>
      <g font-size="7" fill="var(--muted)" text-anchor="middle">
        <text x="642" y="198">-70</text><text x="621" y="149">-40</text><text x="642" y="99">-18</text>
        <text x="691" y="74">-10</text><text x="741" y="99">3</text><text x="761" y="149">20</text><text x="741" y="198">40</text>
      </g>
      <text x="691" y="124" font-size="15" text-anchor="middle" fill="var(--text)">RATE</text>
      <rect x="642" y="132" width="99" height="31" rx="3" fill="#3a3a3a"/>
      <text x="733" y="155" font-size="22" text-anchor="end" fill="#fff" class="mono">-8.1</text>
      <text x="691" y="181" font-size="14" text-anchor="middle" fill="var(--text)">psi / min</text>
    </g>

    <!-- trend gauge -->
    <g class="dial-gauge">
      <circle cx="881" cy="146" r="86" fill="var(--dial)"/>
      <path d="M837.2 189.8 A62 62 0 1 1 924.8 189.8" fill="none" stroke="var(--blue-soft)" stroke-width="5" pathLength="100" stroke-dasharray="0.4 2.1"/>
      <rect x="879" y="76" width="4" height="9" fill="var(--green)"/>
      <path d="M877 92 l4 -6 l4 6z" fill="#ddd"/>
      <text x="881" y="100" font-size="5" text-anchor="middle" fill="var(--muted)">TEST SPEC</text>
      <g font-size="7" fill="var(--muted)" text-anchor="middle">
        <text x="832" y="198">-100</text><text x="811" y="149">-50</text><text x="832" y="99">-25</text>
        <text x="881" y="74">0</text><text x="931" y="99">25</text><text x="951" y="149">50</text><text x="931" y="198">100</text>
      </g>
      <text x="881" y="124" font-size="15" text-anchor="middle" fill="var(--text)">TREND</text>
      <rect x="831" y="132" width="100" height="31" rx="6" fill="#3a3a3a"/>
      <text x="881" y="153" font-size="15" text-anchor="middle" fill="#fff">Improving</text>
    </g>

    <!-- hold percent -->
    <g class="hold-meter">
      <rect x="977" y="58" width="85" height="173" rx="8" fill="var(--readout)"/>
      <rect x="1005" y="70" width="11" height="132" fill="#3a3a3a"/>
      <rect x="1005" y="126" width="11" height="76" fill="#2aa6e8"/>
      <g font-size="7" fill="var(--muted)">
        <text x="1021" y="73">100</text><text x="1021" y="106">75</text><text x="1021" y="139">50</text>
        <text x="1021" y="172">25</text><text x="1021" y="204">0</text>
      </g>
      <text x="1019" y="222" font-size="15" text-anchor="middle" fill="var(--text)">HOLD %</text>
    </g>

    <!-- chart -->
    <g class="chart">
      <rect x="75" y="253" width="946" height="379" fill="var(--plot)"/>
      <rect x="75" y="336" width="946" height="158" fill="var(--teal-band)"/>
      <rect x="663" y="253" width="358" height="379" fill="#ffffff" opacity="0.04"/>
      <g stroke="#3c3c3c" stroke-dasharray="3 3">
        <line x1="141" y1="253" x2="141" y2="632"/><line x1="323" y1="253" x2="323" y2="632"/>
        <line x1="503" y1="253" x2="503" y2="632"/><line x1="683" y1="253" x2="683" y2="632"/>
        <line x1="863" y1="253" x2="863" y2="632"/>
      </g>
      <line x1="663" y1="253" x2="663" y2="632" stroke="var(--period)"/>
      <rect x="663" y="253" width="358" height="17" fill="var(--period)"/>
      <text x="842" y="267" font-size="16" text-anchor="middle" fill="#fff">1 Min Test Period</text>

      <g font-size="10" fill="var(--pink)" text-anchor="end">
        <text x="67" y="296">30</text><text x="67" y="370">25</text><text x="67" y="441">20</text>
        <text x="67" y="513">15</text><text x="67" y="586">10</text>
      </g>
      <text transform="translate(46 405) rotate(-90)" font-size="11" text-anchor="middle" fill="var(--pink)">Temperature</text>
      <g font-size="9" fill="var(--muted)">
        <text x="1029" y="276">1200</text><text x="1029" y="308">1100</text><text x="1029" y="339">1000</text>
        <text x="1029" y="371">900</text><text x="1029" y="402">800</text><text x="1029" y="434">700</text>
        <text x="1029" y="465">600</text><text x="1029" y="497">500</text><text x="1029" y="528">400</text>
        <text x="1029" y="560">300</text><text x="1029" y="591">200</text><text x="1029" y="623">100</text>
      </g>
      <text transform="translate(1060 411) rotate(-90)" font-size="11" text-anchor="middle" fill="var(--blue-soft)">Pressure</text>
      <g font-size="10" fill="#dcdcdc" text-anchor="middle">
        <text x="141" y="650">22:04:30</text><text x="323" y="650">22:05:00</text><text x="503" y="650">22:05:30</text>
        <text x="683" y="650">22:06:00</text><text x="863" y="650">22:06:30</text>
      </g>
      <path d="M862 645 l3 -5 l3 5z" fill="#f0a020"/>

      <path d="M75 292 L377 292 L420 288 L870 291" fill="none" stroke="var(--pink)" stroke-width="2"/>
      <path d="M379 632 L383 615 L386 600 L390 570 L394 545 L398 505 L402 470 L406 440 L410 410 L414 392 L419 384 L663 387 L765 388" fill="none" stroke="var(--blue)" stroke-width="3"/>
      <path d="M765 388 L866 388" stroke="var(--green)" stroke-width="3"/>
      <path d="M866 388 L1021 388" stroke="var(--green)" stroke-width="1.5" stroke-dasharray="5 4"/>
      <circle cx="663" cy="387" r="2.5" fill="var(--blue)"/>
      <circle cx="765" cy="388" r="2.5" fill="var(--blue)"/>
      <circle cx="866" cy="388" r="3" fill="var(--blue)"/>
      <circle cx="1021" cy="388" r="3" fill="var(--green)"/>
      <g font-size="14" fill="var(--blue-soft)" text-anchor="middle">
        <text x="636" y="362">P1</text><text x="641" y="380">844.3</text>
        <text x="741" y="362">P2</text><text x="746" y="380">841.4</text>
        <text x="845" y="362">P3</text><text x="850" y="380">839.0</text>
      </g>
      <text x="1005" y="380" font-size="14" text-anchor="middle" fill="var(--green)">836</text>

      <g class="callout">
        <rect x="295" y="594" width="71" height="22" rx="3" fill="var(--callout)"/>
        <path d="M318 616 l6 7 l6 -7z" fill="var(--callout)"/>
        <text x="330" y="609" font-size="9" font-weight="500" text-anchor="middle" fill="#111">Start operation</text>
      </g>
    </g>
  </svg>

  <aside class="controls">
    <div class="control-btn" style="top:8px">Screen Shot</div>
    <div class="control-btn" style="top:53px">Heave Cancel</div>
    <div class="control-btn active" style="top:98px">Prediction</div>
    <div class="control-btn" style="top:143px">Zoom</div>
    <div class="control-btn" style="top:188px">Snap Halo</div>
    <div class="control-btn" style="top:233px">Reset View</div>
    <div class="control-btn" style="top:558px;height:46px">Lock Hold<br>Period</div>
    <div class="control-btn disabled" style="top:608px">Publish</div>
  </aside>
</body>
</html>
```